"Maple Hollow" red wine label design

We are a Sydney based company. We need to design a wine label for a Australian red wine.
Front label include following info:
Our brand: "Maple Hollow";
Product name: "Shiraz 2016";
In the bottom with small font: "Wine of Australia", "750ml"
Back label:
the back label would need to be consistent with the front label, with space for one paragraph of tasting notes, and ingredient info etc.
we would like to use white, gold and blue in this label. It should make customer feel the magical and beautiful moment of starry night.

We also need a logo design for the wine brand: "Maple Hollow"

I have attached a few wine bottle that used blue to give you some inspirations.

We need the design in AI file format.

Target Market(s)

both men and women

Industry/Entity Type

It Company

Logo Text

Maple Hollow

Requirements
Nice to have
• gold borderline, words; use of blue and white

```html
<!DOCTYPE html>
<html lang="en">
<head>
<meta charset="UTF-8">
<title>Maple Hollow Shiraz 2016 – Front Label</title>
<link rel="stylesheet" href="https://fonts.googleapis.com/css2?family=Cinzel:wght@400;500;600&display=swap">
<style>
  :root {
    --page-bg: #ffffff;
    --night-black: #070704;
    --night-deep: #14130a;
    --night-olive: #35321a;
    --milky-gold: #8a843d;
    --milky-light: #d2cc8c;
    --milky-glow: #b4ad62;
    --forest-dark: #040403;
    --gold-light: #f3c24a;
    --gold-text: #e39a22;
    --gold-deep: #a9600e;
  }
  html, body {
    margin: 0;
    width: 1200px;
    height: 1200px;
    overflow: hidden;
    background: var(--page-bg);
  }
  .canvas {
    position: relative;
    width: 1200px;
    height: 1200px;
    display: flex;
    align-items: center;
    justify-content: center;
  }
  .label {
    position: relative;
    width: 760px;
    height: 960px;
    overflow: hidden;
    font-family: "Cinzel", "Times New Roman", serif;
    color: var(--gold-text);
    text-align: center;
  }
  .label__night-sky {
    position: absolute;
    inset: 0;
    background:
      linear-gradient(to bottom, transparent 0%, transparent 58%, rgba(4, 4, 3, 0.85) 72%, var(--forest-dark) 82%, var(--forest-dark) 100%),
      radial-gradient(ellipse 22% 45% at 12% 12%, var(--milky-light) 0%, transparent 75%),
      radial-gradient(ellipse 35% 30% at 22% 62%, var(--milky-glow) 0%, transparent 80%),
      radial-gradient(ellipse 25% 30% at 88% 68%, var(--night-olive) 0%, transparent 80%),
      linear-gradient(100deg, var(--milky-gold) 0%, var(--milky-glow) 18%, var(--night-olive) 40%, var(--night-deep) 58%, var(--night-black) 75%, var(--night-deep) 100%);
  }
  .label__text {
    position: absolute;
    left: 0;
    right: 0;
    margin: 0;
    font-weight: 500;
    white-space: nowrap;
    background: linear-gradient(to bottom, var(--gold-light) 0%, var(--gold-text) 50%, var(--gold-deep) 100%);
    -webkit-background-clip: text;
    background-clip: text;
    -webkit-text-fill-color: transparent;
    filter: drop-shadow(0 2px 2px rgba(0, 0, 0, 0.7));
  }
  .label__brand {
    top: 215px;
    font-size: 78px;
    font-weight: 600;
    letter-spacing: 1px;
    line-height: 1;
  }
  .label__product {
    top: 318px;
    font-size: 46px;
    font-weight: 400;
  }
  .label__origin {
    top: 780px;
    font-size: 38px;
    font-weight: 400;
  }
  .label__volume {
    top: 850px;
    font-size: 28px;
    font-weight: 400;
  }
</style>
</head>
<body>
  <main class="canvas">
    <section class="label">
      <div class="label__night-sky" role="img" aria-label="Photograph of a golden Milky Way starry night sky over a dark pine forest silhouette"></div>
      <h1 class="label__text label__brand">Maple Hollow</h1>
      <p class="label__text label__product">Shiraz 2016</p>
      <p class="label__text label__origin">Wine of Australia</p>
      <p class="label__text label__volume">750 ML</p>
    </section>
  </main>
</body>
</html>
```